Website Design for Self-Publishing Coaching and Training program

We’re looking to get a website design to represent and deliver a self-publishing coaching and training program called “Page-Bound Path”.

The tag line for the program and the site is “Step-By-Step Training and Personal Coaching to Help Get Your Book out of Your Head and Into the Hands of Your Waiting Avid Readers”.

The program is based around a 6-step process shown in the attached image named “6 Stages for Nova-QR.png” and what makes this program unique is it will provide coaching and training through small coaching groups of a minimum of 4 and no more than 8 participants in any coaching group.

Attached is a PDF export from Balsamiq showing the 5 most unique webpage wireframes for the site to give you an idea of how content for the program will be presented and organized to the site users and presented on different devices with varying screen sizes. If you have access to Balsamiq, I’m also attaching a zip folder for the whole project with all of the bmml files.

What we are looking for specifically is a responsive site design to fit the layout provide in the attached files particularly a color scheme and fonts. Please only use Google Web fonts or Adobe Type Kit Portfolio Fonts available in Adobe CC.

The site design should capture the idea that this is a step-by-step, personal small group coaching to help someone self-publish their first book along with the concepts and emotional end benefits described below.

The website design will be use on a Drupal website and we will convert the best website design to a Drupal Theme ourselves, but we also want to get the html and CSS from you as place to start that process if possible. However, if you are able to provide a fully functional Drupal Theme, we will certainly give your entry more preference.

Our market research tells us that the Features and Emotional Benefits Authors Want in Self-Publishing Coaching Program are:
1. “A Step-by-Step Process” that gives them the Emotional End Benefits of:
• Feeling Safe
• Associated Colors: Green #008000, White #ffffff, Navy #000080
• Being Productive
• Associated Colors: Green #008000, Blue #0000ff, Lime #00ff00
• Feeling Creative
• Associated Colors: Fuchsia #ff00ff, Lime #00ff00, Yellow #ffff00
• Feeling Peaceful - Relaxed – Calm
• Associated Colors: White #ffffff, Aqua #00ffff, Teal #008080, Green #008000

2. “One Reliable, Honest and Expert Source For Everything” that gives them the Emotional End Benefits of:
• Feeling Safe
• Feeling Financially Secure
• Associated Colors: Navy #000080, Green #008000, Blue #0000ff
• A Sense of Belonging
• Associated Colors: Light Browns - sorry don’t have exact hex colors for you for this one but I would guess BurlyWood #DEB887 through Chocolate #D2691E

And the top 3 Emotional End Benefits authors get from publishing a book are:
1. Feeling Respected
• Associated Colors: Red #ff0000, Purple #800080
2. Sense of Accomplishment
• Associated Colors: Gold #FFD700, Red #ff0000, Purple #800080
• Related to this Success
• Associated Colors: Green #008000, Red #ff0000, Yellow #ffff00
3. Feeling Creative

Obviously you do not need to use every exact color sited above. This is just to give you an idea of kinds of emotions we want to evoke with the site and logo colors and the above colors are what we believe will be best associated with those emotions.

We have also found that green was the most often picked color associated with the personality of the coach for this course and green is highly represented with several of the emotions above, so a green color would be best to be the prominent color for the website. Probably a color in the range from “DarkSeaGreen” to “DarkGreen”, but we are flexible about this and look forward to seeing your professional ideas.

DarkSeaGreen HEX: 8F BC 8F
MediumAquamarine HEX: 66 CD AA
MediumSeaGreen HEX: 3C B3 71
SeaGreen   HEX: 2E 8B 57
ForestGreen HEX: 22 8B 22
Green HEX: 00 80 00
DarkGreen HEX: 00 64 00

We also know that prospective clients will see their coach as a “Wizard / Sage” or alchemist who heroically guides the author to self-publish and become a conqueror themselves. This makes the coach their Hero and Guide.

And the expected target audience for will be females ages 45+ (most about age 55) who see themselves as “a Butterfly or Cinderella” because they transform through the process of self-publishing. And they become “Conquerors” through the accomplishment of self-publishing their books which makes them “Movie Stars” for the recognition they will receive for their conquest and transformation.

We do not want a design that overtly uses these Archetypes (Wizard, Sage, Hero, Guide, Butterfly, Cinderella, Conqueror or Movie Star”) but rather we are looking for a design that subtlety suggests these things about the coach and clients through a step-by-step personal process.

Thank you for consideration of this project and we look forward to seeing your creative designs.

We are also running a separate contest for the logo for this site and encourage you to submit to that contest as well.

Target Market(s)

See Project Description

Coding

Coded - Design and coding required

Number of Pages Required

5+ page

Colors
9bcb3b
add136
cadf82
eaf2ce
ffffff

Requirements
Must have
• See Project Description
Nice to have
• See Project Description
Should not have
• See Project Description

```html
<!DOCTYPE html>
<html lang="en">
<head>
<meta charset="utf-8">
<title>Page-Bound Path</title>
<link rel="stylesheet" href="https://fonts.googleapis.com/css2?family=Oswald:wght@400;500&family=Roboto:wght@300;400;500&display=swap">
<style>
:root{
  --green:#9bcb3b;
  --green-2:#add136;
  --green-pale:#cadf82;
  --green-mist:#eaf2ce;
  --white:#ffffff;
  --ink:#222222;
  --muted:#777777;
  --card-bg:#f6f6f6;
  --card-line:#d9d9d9;
  --footer:#1e1e1e;
  --footer-line:#2aa0dc;
  --player:#2a2a2a;
  --player-red:#e9343c;
  --safe:#008000;
  --blue:#0000ff;
  --yellow:#ffff00;
  --fuchsia:#ff00ff;
  --aqua:#00ffff;
}
*{box-sizing:border-box;margin:0;padding:0}
html,body{width:766px;height:1200px;overflow:hidden;background:var(--white)}
body{font-family:"Roboto",Arial,sans-serif;color:var(--ink)}
.page{position:relative;width:766px;height:1200px}
.abs{position:absolute}

/* header */
.brand{left:24px;top:28px;display:flex;align-items:center;gap:8px}
.brand-mark{width:20px;height:20px;background:var(--green)}
.brand-name{font-family:"Oswald",sans-serif;font-size:21px;font-weight:500;color:var(--ink);letter-spacing:.2px}
.tagline{left:318px;top:28px;width:310px;font-size:9.5px;line-height:17px;color:var(--ink)}
.badge{left:636px;top:14px;width:102px;height:52px;border:2px solid #1e3f8f;border-radius:4px;background:#fff}
.badge span{position:absolute;left:3px;right:3px;bottom:3px;height:14px;border:1px solid #1e3f8f}

/* nav */
.nav{left:0;top:76px;width:766px;height:42px;background:linear-gradient(180deg,var(--green-2),var(--green));display:flex;align-items:center;padding-left:24px}
.nav a{color:var(--white);text-decoration:none;font-size:10.5px;height:42px;line-height:42px;padding:0 13px}
.nav a.active{background:#1b1b1b;padding:0 19px}

/* hero */
.hero{left:0;top:118px;width:766px;height:331px;background:linear-gradient(110deg,#3a3530 0%,#4c4239 40%,#2e2a27 70%,#3d3631 100%)}
.video{left:22px;top:169px;width:390px;height:236px;background:var(--white)}
.video-art{position:absolute;left:10px;top:7px;width:370px;height:188px;background:linear-gradient(180deg,#e9e9e9,#fbfbfb)}
.video-play{position:absolute;left:164px;top:80px}
.video-bar{position:absolute;left:10px;top:195px;width:370px;height:31px;background:var(--player)}
.hero-copy{left:440px;top:184px;width:320px;color:var(--white)}
.hero-title{font-family:"Oswald",sans-serif;font-size:30px;font-weight:500;line-height:40px;white-space:nowrap;letter-spacing:-.2px}
.hero-text{font-size:12.5px;line-height:22px;margin-top:4px}
.benefits{list-style:none;margin-top:10px}
.benefits li{display:flex;align-items:center;gap:9px;font-size:14.5px;height:25.5px}
.benefits svg{flex:none}
.c-safe{color:var(--safe)}.c-blue{color:var(--blue)}.c-yellow{color:var(--yellow)}.c-fuchsia{color:var(--fuchsia)}.c-aqua{color:var(--aqua)}

/* cards */
.card{background:var(--card-bg);border:1px solid var(--card-line);box-shadow:0 2px 2px rgba(0,0,0,.12)}
.profile-head{position:absolute;left:0;top:0;right:0;height:104px;background:var(--green);color:var(--white)}
.avatar{position:absolute;left:10px;top:17px;width:70px;height:70px;border-radius:50%;border:3px solid #e9e9e9;background:linear-gradient(160deg,#c9b9a6,#7a6656)}
.profile-name{position:absolute;left:91px;top:22px;font-size:16px}
.profile-role{position:absolute;left:91px;top:42px;font-size:11.5px;color:#f3f8e6}
.profile-note{position:absolute;left:92px;top:61px;width:124px;font-size:9.5px;line-height:14.5px;font-weight:500}
.thumb{position:absolute}
.body-text{position:absolute;font-size:9.8px;line-height:16.5px;color:var(--muted);text-align:justify}
.card-title{position:absolute;left:0;right:0;text-align:center;font-size:17.5px;color:var(--green)}
.card-sub{position:absolute;left:0;right:0;text-align:center;font-size:12.5px;color:#444}
.btn{position:absolute;background:var(--green);color:var(--white);font-size:10.5px;text-align:center;border-radius:2px}
.feature-title{position:absolute;left:0;right:0;text-align:center;font-size:17.5px;font-weight:500;color:var(--ink)}
.feature-sub{position:absolute;left:0;right:0;text-align:center;font-size:14px;color:#333}
.feature-text{position:absolute;left:10px;right:10px;text-align:center;font-size:10.4px;line-height:20px;font-weight:300;color:var(--muted);white-space:nowrap}

/* footer */
.footer-line{left:0;top:1112px;width:766px;height:4px;background:var(--footer-line)}
.footer{left:0;top:1116px;width:766px;height:84px;background:var(--footer);color:var(--white)}
.footer-links{position:absolute;left:27px;top:27px;font-size:11px}
.footer-links span{margin:0 6px;color:#bbb}
.copyright{position:absolute;left:27px;top:47px;font-size:11px}
.social{position:absolute;top:28px;width:25px;height:25px}
</style>
</head>
<body>
<div class="page">

  <header>
    <div class="brand abs"><span class="brand-mark"></span><span class="brand-name">Page-Bound Path</span></div>
    <p class="tagline abs">“StepByStep Training and Personal Coaching to Help Get Your Book out of Your Head and Into the Hands of Your Waiting Avid Readers”.</p>
    <div class="badge abs" role="img" aria-label="Membership badge"><span></span></div>
  </header>

  <nav class="nav abs">
    <a class="active">HOME</a>
    <a>FREE WORKSHOPS</a>
    <a>ATO Z TRAINING LIBRARY</a>
    <a>COACHING PROGRAMS</a>
    <a>FAQ,S</a>
    <a>SELF-PUBLISHING WIZARD BLOG</a>
  </nav>

  <section class="hero abs" role="img" aria-label="Woman reading among library bookshelves, darkened backdrop"></section>

  <div class="video abs">
    <div class="video-art" role="img" aria-label="Video still: the six-step self-publishing cycle diagram"></div>
    <svg class="video-play" width="42" height="42" viewBox="0 0 42 42"><circle cx="21" cy="21" r="21" fill="#555" fill-opacity=".8"/><path d="M15 11L32 21L15 31z" fill="#fff"/></svg>
    <div class="video-bar">
      <svg width="370" height="31" viewBox="0 0 370 31" font-family="Roboto, sans-serif">
        <circle cx="20" cy="15.5" r="6.5" fill="none" stroke="#fff" stroke-width="1.3"/><path d="M18 12L23.5 15.5L18 19z" fill="#fff"/>
        <path d="M38 13h2.5l3.5-2.5v10l-3.5-2.5H38z" fill="var(--player-red)"/>
        <g fill="var(--player-red)"><rect x="56" y="12" width="1.6" height="7"/><rect x="59" y="12" width="1.6" height="7"/><rect x="62" y="12" width="1.6" height="7"/><rect x="65" y="12" width="1.6" height="7"/></g>
        <rect x="93" y="15" width="162" height="1.6" fill="#666"/><rect x="93" y="14" width="58" height="3.2" rx="1.6" fill="var(--player-red)"/>
        <text x="266" y="19" font-size="7.6" fill="#fff">01:30 / 04:55</text>
        <rect x="327" y="12" width="10" height="7" fill="none" stroke="#fff" stroke-width="1.3"/>
        <circle cx="352" cy="15.5" r="4" fill="none" stroke="#fff" stroke-width="2" stroke-dasharray="1.6 1.2"/>
      </svg>
    </div>
  </div>

  <div class="hero-copy abs">
    <h1 class="hero-title">A STEP BY STEP PROCESS</h1>
    <p class="hero-text">Lorem Ipsum has been the industry's standard dummy text ever since the 1500s, when an unknown printer</p>
    <ul class="benefits">
      <li><svg width="12" height="12" viewBox="0 0 12 12"><circle cx="6" cy="6" r="6" fill="#fff"/><path d="M3 6.2l2 2 4-4" stroke="#333" stroke-width="1.6" fill="none"/></svg><span>FEELING <span class="c-safe">SAFE</span></span></li>
      <li><svg width="12" height="12" viewBox="0 0 12 12"><circle cx="6" cy="6" r="6" fill="#fff"/><path d="M3 6.2l2 2 4-4" stroke="#333" stroke-width="1.6" fill="none"/></svg><span><span class="c-blue">BEING</span> PRODUCTIVE</span></li>
      <li><svg width="12" height="12" viewBox="0 0 12 12"><circle cx="6" cy="6" r="6" fill="#fff"/><path d="M3 6.2l2 2 4-4" stroke="#333" stroke-width="1.6" fill="none"/></svg><span><span class="c-yellow">FEELING</span> <span class="c-fuchsia">CREATIVE</span></span></li>
      <li><svg width="12" height="12" viewBox="0 0 12 12"><circle cx="6" cy="6" r="6" fill="#fff"/><path d="M3 6.2l2 2 4-4" stroke="#333" stroke-width="1.6" fill="none"/></svg><span><span class="c-aqua">FEELING</span> PEACEFUL &nbsp;<span class="c-safe">RELAXED</span> – CALM</span></li>
    </ul>
  </div>

  <article class="card abs" style="left:24px;top:471px;width:226px;height:247px">
    <div class="profile-head">
      <div class="avatar" role="img" aria-label="Coach portrait"></div>
      <div class="profile-name">NORA VALE</div>
      <div class="profile-role">- Sating The Preta</div>
      <div class="profile-note">Lorem Ipsum has been the industry's standard dummy</div>
    </div>
    <div class="thumb" role="img" aria-label="Report cover with orange design" style="left:8px;top:123px;width:75px;height:106px;background:linear-gradient(160deg,#f1f1f1 45%,#e8793a 46%,#c9481c)"></div>
    <p class="body-text" style="left:92px;top:127px;width:122px">Lorem Ipsum has been the industry's standard dummy text ever since the 1500s, when an unknown printer took a galley of type and scrambled it to make</p>
  </article>

  <article class="card abs" style="left:262px;top:471px;width:241px;height:247px">
    <div class="card-title" style="top:15px">Neque porro quisquam</div>
    <div class="card-sub" style="top:40px">Dolorem ipsum quia</div>
    <div class="thumb" role="img" aria-label="Magazine cover with green design" style="left:14px;top:77px;width:74px;height:132px;background:linear-gradient(170deg,#8ec63f,#4f8f2a 55%,#e8e8e8 56%,#cfcfcf)"></div>
    <p class="body-text" style="left:101px;top:85px;width:126px">Lorem Ipsum has been the industry's standard dummy text ever since the 1500s, when an unknown printer took a galley of type and scrambled it to make a type</p>
    <div class="btn" style="left:103px;top:187px;width:68px;height:25px;line-height:25px">Read More</div>
  </article>

  <article class="card abs" style="left:515px;top:471px;width:226px;height:247px">
    <div class="profile-head">
      <div class="avatar" role="img" aria-label="Coach portrait"></div>
      <div class="profile-name">NORA VALE</div>
      <div class="profile-role">- Sating The Preta</div>
      <div class="profile-note">Lorem Ipsum has been the industry's standard dummy</div>
    </div>
    <div class="thumb" role="img" aria-label="Business headline cover with city skyline" style="left:10px;top:118px;width:77px;height:107px;border:1px solid #ddd;background:linear-gradient(180deg,#f6e3b8,#e7a24a 45%,#b8312c 65%,#ffffff 66%)"></div>
    <p class="body-text" style="left:98px;top:122px;width:118px">Lorem Ipsum has been the industry's standard dummy text ever since the 1500s, when an unknown printer took a galley of type and scrambled it to make</p>
  </article>

  <article class="card abs" style="left:24px;top:744px;width:347px;height:334px">
    <div class="thumb" role="img" aria-label="Woman reading a book outdoors on grass" style="left:15px;top:11px;width:317px;height:153px;background:linear-gradient(120deg,#8a7a3e,#5a4a2a 45%,#c9b98a 70%,#6c5a34)"></div>
    <div class="feature-title" style="top:186px">Neque porro quisquam est</div>
    <div class="feature-sub" style="top:210px">Dolorem ipsum quia</div>
    <p class="feature-text" style="top:234px">Lorem Ipsum has been the industry's standard dummy text ever<br>since the 1500s, when an unknown printer took a galley of type</p>
    <div class="btn" style="left:135px;top:284px;width:78px;height:29px;line-height:29px;font-size:11.5px">Read More</div>
  </article>

  <article class="card abs" style="left:395px;top:744px;width:347px;height:334px">
    <div class="thumb" role="img" aria-label="Woman with glasses reading a book at a desk, video" style="left:17px;top:12px;width:315px;height:191px;background:linear-gradient(120deg,#6f7a80,#b7b2a8 45%,#e2c08a 60%,#8e8a84)">
      <svg class="abs" style="left:132px;top:70px" width="52" height="52" viewBox="0 0 52 52"><circle cx="26" cy="26" r="26" fill="#333" fill-opacity=".8"/><path d="M20 15L37 26L20 37z" fill="#fff"/></svg>
    </div>
    <div class="feature-title" style="top:220px">Neque porro quisquam est</div>
    <div class="feature-sub" style="top:244px">Dolorem ipsum quia</div>
    <div class="btn" style="left:135px;top:274px;width:78px;height:29px;line-height:29px;font-size:11.5px">Read More</div>
  </article>

  <div class="footer-line abs"></div>
  <footer class="footer abs">
    <div class="footer-links">Privacy Policy<span>|</span>Terms of Use<span>|</span>About Us<span>|</span>Sitemap</div>
    <div class="copyright">Copyright © 2016&nbsp; All Rights</div>
    <div class="social" role="img" aria-label="Social link" style="left:618px;background:#2aa0dc"></div>
    <div class="social" role="img" aria-label="Video channel link" style="left:651px;background:#d8322b"></div>
    <div class="social" role="img" aria-label="Social link" style="left:684px;background:#3b5998"></div>
    <div class="social" role="img" aria-label="Professional network link" style="left:717px;background:#1a7ab8"></div>
  </footer>

</div>
</body>
</html>
```